Brightfield Co Trade Show Flyer

We need a brochure design (8.5 x 11) Info in the design (refer to rough draft I drew on Paper): "#1 selling tool to aquire new franchisees has been video testimonials" - Martin L. Crowe, C.E.O Tovik Smoothie Franchise Testimonials - Let your franchisees do the selling for you. Franchisee testimonial: $10,000 / per Franchisee Includes: • 2 minute Video • 1 minute add for your franchise's location • Concept creation • Communication with franchisee • Travel to their location • All rental equipment • 1 round of corrections • Animated logo • Licensed music ******* For 25% Discount section (next to middle box), please put the "Outlet Summit Logo" Great to use on all your social media (USE logos and icons) • Website • YouTube • LinkedIn • Facebook • Instagram • Twitter • Phone calls • Emails • In person meetings Some of our clients: (use the logos I uploaded - in round boxes as in draft) LOGO (Brightfield Franchise Testimonial) www.brightfieldvoices.example (866) 555-0172

Target Market(s)

Franchise owners

Colors

Designer to choose colors to be used in the design.

Requirements

```html
<!DOCTYPE html>
<html lang="en">
<head>
<meta charset="utf-8">
<title>Brightfield Co Trade Show Flyer</title>
<link href="https://fonts.googleapis.com/css2?family=Archivo+Black&family=Exo+2:ital,wght@1,700;1,800&family=Montserrat:wght@700;800;900&family=Source+Sans+3:ital,wght@0,400;0,600;0,700;1,400&display=swap" rel="stylesheet">
<style>
  :root {
    --red: #ed1b3c;
    --ink: #4a4b4e;
    --black: #111111;
    --teal: #13aa93;
    --paper: #ffffff;
  }
  * { margin: 0; padding: 0; box-sizing: border-box; }
  html, body { width: 945px; height: 1200px; overflow: hidden; background: var(--paper); }
  .flyer { position: relative; width: 945px; height: 1200px; background: var(--paper); overflow: hidden; font-family: "Source Sans 3", sans-serif; }
  .abs { position: absolute; }

  .quote-mark { left: 76px; top: 20px; font-family: "Archivo Black", sans-serif; font-size: 150px; line-height: 1; color: var(--red); }
  .quote-text { left: 183px; top: 60px; font-size: 18px; font-weight: 700; color: var(--black); white-space: nowrap; }
  .quote-author { right: 79px; top: 91px; font-size: 17px; font-style: italic; color: var(--black); white-space: nowrap; }

  .headline { left: 0; top: 160px; }

  .speech-shape { left: 0; top: 0; }

  .tagline { left: 462px; top: 338px; font-family: "Source Sans 3", sans-serif; font-weight: 700; font-size: 33px; line-height: 40px; color: var(--red); text-transform: uppercase; }

  .discount-figure { left: 282px; top: 500px; }
  .discount-label { left: 282px; top: 626px; font-family: "Archivo Black", sans-serif; font-size: 32px; line-height: 1; color: var(--teal); letter-spacing: 0.5px; }

  .summit-badge { left: 622px; top: 514px; width: 236px; height: 130px; background: var(--teal); padding: 12px 0 0 12px; font-family: "Archivo Black", sans-serif; font-size: 31px; line-height: 29px; color: var(--paper); }
  .summit-motto { left: 622px; top: 648px; width: 236px; text-align: center; font-family: "Montserrat", sans-serif; font-weight: 800; font-size: 11px; letter-spacing: 1px; color: var(--teal); }

  .package { left: 145px; top: 690px; color: var(--paper); font-family: "Exo 2", sans-serif; font-style: italic; }
  .package-title { font-weight: 800; font-size: 21px; line-height: 23px; margin-bottom: 6px; }
  .package-list { list-style: none; }
  .package-list li { position: relative; padding-left: 28px; font-weight: 700; font-size: 18px; line-height: 23px; margin-bottom: 4px; }
  .package-list li svg { position: absolute; left: 0; top: 4px; }

  .reach-title { left: 503px; top: 728px; width: 400px; text-align: center; font-family: "Montserrat", sans-serif; font-weight: 800; font-size: 22px; line-height: 25px; color: var(--black); }
  .reach-title em { font-style: normal; color: var(--red); }
  .channels { left: 0; top: 0; }

  .brand-mark { left: 658px; top: 884px; width: 80px; height: 80px; border-radius: 50%; background: var(--black); }
  .brand-name { left: 503px; top: 994px; width: 400px; text-align: center; font-family: "Archivo Black", sans-serif; font-size: 45px; line-height: 1; color: var(--black); }
  .brand-sub { left: 503px; top: 1047px; width: 400px; text-align: center; font-family: "Montserrat", sans-serif; font-weight: 700; font-size: 12px; color: var(--black); }

  .website { left: 503px; top: 1093px; width: 400px; text-align: center; font-family: "Source Sans 3", sans-serif; font-weight: 700; font-size: 22px; color: var(--red); }
  .phone-icon { left: 552px; top: 1129px; width: 36px; height: 35px; background: var(--red); border-radius: 3px; }
  .phone-number { left: 596px; top: 1122px; font-family: "Montserrat", sans-serif; font-weight: 700; font-size: 31px; line-height: 1.2; color: var(--ink); white-space: nowrap; }

  .trusted-label { left: 176px; top: 1091px; width: 175px; text-align: center; font-size: 13px; color: var(--ink); letter-spacing: 0.5px; }
  .trusted-label::before, .trusted-label::after { content: ""; display: inline-block; width: 30px; height: 1px; background: var(--ink); vertical-align: middle; margin: 0 5px; }
  .client-badges { left: 0; top: 0; }

  .footer-band { left: 90px; top: 1188px; width: 778px; height: 20px; background: var(--red); border-radius: 10px 10px 0 0; }
</style>
</head>
<body>
<main class="flyer">

  <svg class="abs speech-shape" width="945" height="1200" aria-hidden="true">
    <path fill="var(--red)" d="M383 341 L414 341 Q434 341 434 361 L434 448 Q434 471 410 471 L385 471 Q238 474 225 584 Q220 600 220 617 Q222 679 330 679 L363 679 Q464 690 464 787 L464 990 Q464 1075 379 1075 L160 1075 Q81 1075 81 990 L81 584 Q98 347 383 341 Z"/>
  </svg>

  <div class="abs quote-mark">&ldquo;</div>
  <p class="abs quote-text">#1 selling tool to aquire new franchisees has been video testimonials&rdquo;</p>
  <p class="abs quote-author">- Martin L. Crowe, C.E.O Tovik Smoothie</p>

  <svg class="abs headline" width="945" height="160" aria-label="Franchise Testimonials">
    <text x="69" y="85" font-family="Montserrat, sans-serif" font-weight="900" font-size="96" fill="var(--ink)" textLength="628" lengthAdjust="spacingAndGlyphs">FRANCHISE</text>
    <text x="67" y="156" font-family="Montserrat, sans-serif" font-weight="900" font-size="96" fill="var(--ink)" textLength="811" lengthAdjust="spacingAndGlyphs">TESTIMONIALS</text>
  </svg>

  <h2 class="abs tagline">Let your<br>franchisees do the<br>selling for you.</h2>

  <svg class="abs discount-figure" width="310" height="120" aria-label="25%">
    <text x="7" y="116" font-family="Archivo Black, sans-serif" font-size="140" fill="var(--red)" textLength="294" lengthAdjust="spacingAndGlyphs">25%</text>
  </svg>
  <div class="abs discount-label">DISCOUNT FOR</div>

  <div class="abs summit-badge">The<br>Outlet<br>Summit</div>
  <div class="abs summit-motto">OWN YOUR OWN BUSINESS!</div>

  <section class="abs package">
    <h3 class="package-title">$10,000 / per<br>Franchisee Includes:</h3>
    <ul class="package-list">
      <li><svg width="18" height="18" viewBox="0 0 18 18"><circle cx="9" cy="9" r="9" fill="var(--black)"/><path d="M4.5 9.2 L7.6 12 L13.5 6" stroke="#fff" stroke-width="2.4" fill="none"/></svg>2 minute Video</li>
      <li><svg width="18" height="18" viewBox="0 0 18 18"><circle cx="9" cy="9" r="9" fill="var(--black)"/><path d="M4.5 9.2 L7.6 12 L13.5 6" stroke="#fff" stroke-width="2.4" fill="none"/></svg>1 minute add for your<br>franchise&rsquo;s location</li>
      <li><svg width="18" height="18" viewBox="0 0 18 18"><circle cx="9" cy="9" r="9" fill="var(--black)"/><path d="M4.5 9.2 L7.6 12 L13.5 6" stroke="#fff" stroke-width="2.4" fill="none"/></svg>Concept creation</li>
      <li><svg width="18" height="18" viewBox="0 0 18 18"><circle cx="9" cy="9" r="9" fill="var(--black)"/><path d="M4.5 9.2 L7.6 12 L13.5 6" stroke="#fff" stroke-width="2.4" fill="none"/></svg>Communication with<br>franchisee</li>
      <li><svg width="18" height="18" viewBox="0 0 18 18"><circle cx="9" cy="9" r="9" fill="var(--black)"/><path d="M4.5 9.2 L7.6 12 L13.5 6" stroke="#fff" stroke-width="2.4" fill="none"/></svg>Travel to their location</li>
      <li><svg width="18" height="18" viewBox="0 0 18 18"><circle cx="9" cy="9" r="9" fill="var(--black)"/><path d="M4.5 9.2 L7.6 12 L13.5 6" stroke="#fff" stroke-width="2.4" fill="none"/></svg>All rental equipment</li>
      <li><svg width="18" height="18" viewBox="0 0 18 18"><circle cx="9" cy="9" r="9" fill="var(--black)"/><path d="M4.5 9.2 L7.6 12 L13.5 6" stroke="#fff" stroke-width="2.4" fill="none"/></svg>1 round of corrections</li>
      <li><svg width="18" height="18" viewBox="0 0 18 18"><circle cx="9" cy="9" r="9" fill="var(--black)"/><path d="M4.5 9.2 L7.6 12 L13.5 6" stroke="#fff" stroke-width="2.4" fill="none"/></svg>Animated logo</li>
      <li><svg width="18" height="18" viewBox="0 0 18 18"><circle cx="9" cy="9" r="9" fill="var(--black)"/><path d="M4.5 9.2 L7.6 12 L13.5 6" stroke="#fff" stroke-width="2.4" fill="none"/></svg>Licensed music</li>
    </ul>
  </section>

  <h3 class="abs reach-title">USE YOUR <em>TESTIMONIALS</em><br>EVERYWHERE</h3>

  <svg class="abs channels" width="945" height="1200" aria-label="Channels: website, video, social networks, phone, email">
    <g fill="var(--red)">
      <circle cx="538" cy="808" r="17"/>
      <circle cx="583" cy="808" r="17"/>
      <circle cx="632" cy="808" r="17"/>
      <circle cx="680" cy="808" r="17"/>
      <circle cx="729" cy="808" r="17"/>
      <circle cx="778" cy="808" r="17"/>
      <circle cx="827" cy="808" r="17"/>
      <circle cx="871" cy="808" r="17"/>
    </g>
    <g stroke="#fff" stroke-width="1.6" fill="none">
      <circle cx="538" cy="808" r="9"/>
      <ellipse cx="538" cy="808" rx="4" ry="9"/>
      <line x1="529" y1="808" x2="547" y2="808"/>
      <rect x="821" y="797" width="12" height="21" rx="2"/>
      <rect x="862" y="801" width="18" height="13" rx="1"/>
      <path d="M862 801 L871 809 L880 801"/>
    </g>
  </svg>

  <div class="abs brand-mark" aria-hidden="true"></div>
  <div class="abs brand-name">BRIGHTFIELD</div>
  <div class="abs brand-sub">&mdash; FRANCHISE TESTIMONIALS &mdash;</div>

  <div class="abs website">www.brightfieldvoices.example</div>
  <div class="abs phone-icon">
    <svg width="36" height="35" viewBox="0 0 36 35" aria-hidden="true"><path d="M12 8 L16 8 L17 13 L14.5 15 Q17 21 22 23 L24 20.5 L29 21.5 L29 25.5 Q28 28 25 28 Q11 26 9 12 Q9 9 12 8 Z" fill="#fff"/></svg>
  </div>
  <div class="abs phone-number">(866) 555-0172</div>

  <div class="abs trusted-label">TRUSTED BY</div>
  <svg class="abs client-badges" width="945" height="1200" aria-label="Client badges">
    <circle cx="166" cy="1147" r="26" fill="none" stroke="var(--red)" stroke-width="3"/>
    <rect x="208" y="1120" width="34" height="54" fill="#e8612c"/>
    <circle cx="285" cy="1147" r="22" fill="#f2c14e"/>
    <rect x="333" y="1122" width="38" height="50" fill="#233e8b"/>
    <rect x="389" y="1126" width="82" height="40" fill="#ffe600"/>
  </svg>

  <div class="abs footer-band"></div>
</main>
</body>
</html>
```